Vostra Capital Web Design

Vostra Capital Limited Shenzhen

This project is a 10 page launch website.
Our client is seeking a contemporary homepage design for a Holdings company. Once we are happy with the homepage design and select designer we will request a secondary page design.

Please see attached company LOGO for an idea of style, it incorporates the traditional Chinese furniture lattice work. The Coral Dune website is one of our clients favorite so we would like to see a similar homepage design to this website.

Use the websites below for reference purpose. The first two are Chinese and the second two are international. We would like to see elements of both but more focus on international design.

http://www.evergrande.com/http://www.orliqueholdings.example/pub/default.aspx http://www.coraldune.example/zh/resort_kelvanoru/
http://www.velde-studio.example
http://img-store-a1.picvault.example/originals/4f/a2/91/4fa291c03b7e55d1a86e20f9c4b713ee.jpg

Company Background
VOSTRA CAPITAL, located in Qianhai, China, is a new real-estate project operator, structuring urban-rural real-estate investment and development, and industrial fund investment. The company also invests in supply chain management and supporting infrastructures. To create new spaces and livable cities Vostra Capital develop win-win strategic partnerships with a number of institutions. Currently cooperating with Marlow East Fenbrook, China urban and rural integrated demonstration.

Target Market(s)

B2B property investment. Target market customers are senior level management/decision makers of large corporations. Focusing geographically on the domestic market first and expanding internationally in 2nd and 3rd years.

Industry/Entity Type

Investment

Requirements
Must have
• Since this is a new company, we would like to the website representing growth and power, E.g. like a growing tree.
Should not have
• Low-level vectors such as curency symbols, American dollar.

```html
<!DOCTYPE html>
<html lang="en">
<head>
<meta charset="utf-8">
<title>Vostra Capital</title>
<link href="https://fonts.googleapis.com/css2?family=Cormorant+SC:wght@600;700&family=PT+Sans:wght@400;700&display=swap" rel="stylesheet">
<style>
:root{
  --bg-deep:#1e1e1e;
  --bg-header:#2a2a2a;
  --bg-welcome:#262626;
  --bg-projects:#2d2d2d;
  --bg-footer:#252525;
  --gold:#c9a33e;
  --gold-light:#e0bf5a;
  --gold-dark:#9c7a26;
  --line:#3c3c3c;
  --text:#f2f2f2;
  --muted:#d8d8d8;
}
*{margin:0;padding:0;box-sizing:border-box}
html,body{width:1045px;height:1200px;overflow:hidden;background:var(--bg-deep)}
body{font-family:"PT Sans",Arial,sans-serif;color:var(--text);position:relative}
.abs{position:absolute}
.heading{font-family:"Cormorant SC",Georgia,serif;font-weight:700;color:var(--gold)}
a{color:inherit;text-decoration:none}

/* top bar */
.top-bar{left:0;top:0;width:1045px;height:36px;background:var(--bg-header);border-bottom:1px solid var(--line)}
.top-links{right:200px;top:11px;font-size:11px}
.lang{left:854px;top:7px;width:64px;height:22px;background:linear-gradient(var(--gold-light),var(--gold-dark));border-radius:2px;font-size:11px;padding:4px 0 0 5px;color:#fff}
.lang span{position:absolute;right:0;top:0;width:16px;height:22px;border-left:1px solid #7a5d1a;font-size:8px;text-align:center;line-height:22px;color:#4a3810}

/* header */
.header{left:0;top:37px;width:1045px;height:89px;background:var(--bg-header)}
.brand{left:135px;top:49px;display:flex;align-items:center;gap:12px}
.brand-mark{width:68px;height:68px;border-radius:50%;border:2px solid var(--gold)}
.brand-name{font-family:"Cormorant SC",Georgia,serif;font-weight:600;font-size:28px;color:var(--gold);letter-spacing:.5px}
.btn{top:61px;height:28px;background:linear-gradient(var(--gold-light),var(--gold-dark));border-radius:2px;font-size:14px;color:#fff;text-align:center;line-height:28px}
.nav-tab{left:420px;top:103px}
.nav{left:453px;top:108px;font-size:12.5px;color:#fff;word-spacing:1px}
.gold-rule{left:0;top:125px;width:1045px;height:3px;background:var(--gold)}

/* hero */
.hero{left:0;top:128px;width:1045px;height:319px;background:linear-gradient(180deg,#6f9ed6 0%,#a9c8e6 45%,#3d6f98 48%,#2e5f86 56%,#d8cdb0 62%,#4f8a3c 75%,#2d5a26 100%)}
.hero-caption{left:245px;top:421px}
.hero-caption-text{left:245px;top:426px;width:585px;text-align:center;font-size:16px;color:#fff}
.hero-arrow{top:425px;font-size:14px;color:#fff}

/* welcome */
.welcome{left:0;top:447px;width:1045px;height:227px;background:var(--bg-welcome);border-bottom:1px solid var(--line)}
.welcome-title{left:135px;top:478px;font-size:30px}
.welcome-text{left:135px;top:521px;width:510px;font-size:12.3px;line-height:16px}
.divider-v{width:1px;background:#5a4a25}
.news-title{left:710px;top:484px;font-size:22px}
.news-item{left:708px;width:212px;font-size:11px;line-height:15px;border-bottom:1px solid #444;padding-bottom:6px}
.news-item .date{display:block;margin-bottom:0}
.news-item .hl{color:var(--gold)}
.news-item .more{float:right;text-decoration:underline}

/* projects */
.projects{left:0;top:674px;width:1045px;height:298px;background:var(--bg-projects);border-bottom:1px solid var(--line)}
.projects-title{left:136px;top:772px;font-size:44px;font-weight:600}
.view-all{left:141px;top:823px;font-size:17px;font-weight:600;border-bottom:1px solid #555;padding-bottom:2px}
.project{width:160px;text-align:center}
.project h3{font-size:12.5px;color:var(--gold);font-weight:700;margin-bottom:8px}
.project-photo{width:159px;height:121px;border:2px solid var(--gold);margin:0 auto}
.project p{font-size:11px;line-height:14px;margin-top:10px}
.project .read{display:inline-block;margin-top:5px;font-size:11.5px;font-weight:700;text-decoration:underline}

/* footer */
.footer{left:0;top:973px;width:1045px;height:188px;background:var(--bg-footer)}
.foot-title{font-size:21px}
.contact{left:135px;top:1031px;width:200px;font-size:11px;line-height:14px}
.contact div{border-bottom:1px solid #4a4a4a;padding:3px 0 4px}
.contact div:last-child{border:0}
.share{left:399px;top:1029px;width:128px;font-size:11px}
.share-row{display:flex;justify-content:space-between;align-items:center;height:28px;border-bottom:1px solid #444}
.share-row:last-child{border:0}
.sq{width:20px;height:20px;border-radius:3px}
.testimonial{left:595px;top:1032px;width:335px;font-size:11px;line-height:14px}
.testimonial .author{color:var(--gold);font-weight:700;margin-top:8px}
.testimonial .all{margin-top:16px}
.bottom-bar{left:0;top:1161px;width:1045px;height:39px;background:var(--bg-header);border-top:1px solid var(--line);font-size:11px}
</style>
</head>
<body>

<div class="abs top-bar"></div>
<div class="abs top-links">Sitemap | Social | Latest Offers</div>
<div class="abs lang">English<span>▼</span></div>

<header>
  <div class="abs header"></div>
  <div class="abs brand">
    <div class="brand-mark"></div>
    <div class="brand-name">Vostra Capital</div>
  </div>
  <a class="abs btn" style="left:716px;width:98px">Destinations</a>
  <a class="abs btn" style="left:819px;width:99px">Experiences</a>
  <svg class="abs nav-tab" width="525" height="23" viewBox="0 0 525 23">
    <path d="M0 23 C12 23 14 0 30 0 H495 C511 0 513 23 525 23 Z" fill="var(--gold)"/>
  </svg>
  <nav class="abs nav">Home &nbsp;|&nbsp; Our Projects &nbsp;|&nbsp; Our Services &nbsp;|&nbsp; Find a Venue &nbsp;|&nbsp; Our Co-Partners &nbsp;|&nbsp; Contact Us</nav>
  <div class="abs gold-rule"></div>
</header>

<section>
  <div class="abs hero" role="img" aria-label="Coastal resort with golf course, palm trees, sandy beach and blue sea"></div>
  <svg class="abs hero-caption" width="585" height="26" viewBox="0 0 585 26">
    <path d="M12 0 H573 L585 26 H0 Z" fill="var(--gold)" opacity=".9"/>
  </svg>
  <div class="abs hero-caption-text">We Are Real-Estate Project Operator</div>
  <div class="abs hero-arrow" style="left:265px">←</div>
  <div class="abs hero-arrow" style="left:792px">→</div>
</section>

<section>
  <div class="abs welcome"></div>
  <h1 class="abs heading welcome-title">Welcome to Vostra Capital</h1>
  <p class="abs welcome-text">&nbsp;We are located in Qianhai, China, is a new real-estate project operator, structuring urban-rural real-estate investment and development, and industrial fund investment. The company also invests in supply chain management and supporting infrastructures. To create new spaces and livable cities Vostra Capital develop win-win strategic partnerships with a number of institutions. Currently cooperating with Marlow East Fenbrook, China urban and rural integrated demonstration.</p>
  <div class="abs divider-v" style="left:670px;top:479px;height:172px"></div>
  <h2 class="abs heading news-title">Latest News/Events</h2>
  <div class="abs news-item" style="top:521px"><span class="date">25-12-2013</span><span class="hl">Lorem Ipsum is simply</span> dummy text of the &nbsp;printing and typesetting industry. <span class="more">More</span></div>
  <div class="abs news-item" style="top:582px;border:0"><span class="date">25-12-2013</span><span class="hl">Lorem Ipsum is simply</span> dummy text of the &nbsp;printing and typesetting industry. <span class="more">More</span></div>
</section>

<section>
  <div class="abs projects"></div>
  <h2 class="abs heading projects-title">Our Projects</h2>
  <a class="abs heading view-all">View All</a>
  <div class="abs project" style="left:407px;top:714px">
    <h3>Title of Project</h3>
    <div class="project-photo" role="img" aria-label="Hillside villas over a green golf course at sunset" style="background:linear-gradient(180deg,#e9b48a,#c98d6a 45%,#4e7a33 70%,#6aa13f)"></div>
    <p>It was popularised in the 1960s with the release of Letraset sheets containing.</p>
    <a class="read">Read More</a>
  </div>
  <div class="abs project" style="left:584px;top:714px">
    <h3>Title of Project</h3>
    <div class="project-photo" role="img" aria-label="Modern glass office building at dusk" style="background:linear-gradient(180deg,#1f2d4a,#3b4f6e 50%,#7f8790 75%,#3a3a32)"></div>
    <p>It was popularised in the 1960s with the release of Letraset sheets containing.</p>
    <a class="read">Read More</a>
  </div>
  <div class="abs project" style="left:761px;top:714px">
    <h3>Title of Project</h3>
    <div class="project-photo" role="img" aria-label="Mediterranean villa with swimming pool and flower garden" style="background:linear-gradient(180deg,#4a7fd0,#9fb8d8 35%,#c48a52 50%,#2f8fbf 70%,#c24a7a)"></div>
    <p>It was popularised in the 1960s with the release of Letraset sheets containing.</p>
    <a class="read">Read More</a>
  </div>
</section>

<footer>
  <div class="abs footer"></div>
  <h3 class="abs heading foot-title" style="left:135px;top:1003px">Contact Information</h3>
  <div class="abs contact">
    <div>Address: Keling Trade Plaza,<br>Keling Rail Terminal, Shenzhen</div>
    <div>Email: reservations@vostracapital.example</div>
    <div>Tel: 011 86 755 0192</div>
    <div>Fax: 011 86 755 0193</div>
  </div>
  <div class="abs divider-v" style="left:367px;top:997px;height:145px"></div>
  <h3 class="abs heading foot-title" style="left:399px;top:1003px">Share With Us:</h3>
  <div class="abs share">
    <div class="share-row">Find Us on <span class="sq" style="background:#3b5998"></span></div>
    <div class="share-row">Tweet on <span class="sq" style="background:#29a9e1"></span></div>
    <div class="share-row">Watch our video on <span class="sq" style="background:#d9382f"></span></div>
    <div class="share-row">Connect us on <span class="sq" style="background:#d4483a"></span></div>
  </div>
  <div class="abs divider-v" style="left:565px;top:997px;height:145px"></div>
  <h3 class="abs heading foot-title" style="left:593px;top:1003px">Testimonials</h3>
  <div class="abs testimonial">
    <p>Lorem Ipsum is simply dummy text of the printing and typesetting industry. Lorem Ipsum has been the industry's standard dummy text ever since the 1500s, when an unknown printer took a galley of type and scrambled it to make a type specimen book.</p>
    <p class="author">John Doe | C.E.O.</p>
    <p class="all">View All</p>
  </div>
  <div class="abs bottom-bar">
    <span class="abs" style="left:135px;top:12px">Copyright © 2013 Vostra Capital | All Rights Reserved</span>
    <span class="abs" style="left:633px;top:13px">Home | About Us | Terms &amp; Uses | Privacy Policy | Contact Us</span>
  </div>
</footer>

</body>
</html>
```